Quirky Label Design for an Exciting UK-Based Organic Skincare Company!

We need label designs across our range of products, we are a high quality yet quirky organic skincare company called Gently Velvety, we use frosted glass packaging, and we are just wanting one design done for now, but the winning designer we would want to work with to design the rest of the labels for us. We also want them to design business cards and other literature at some point and maybe even a website page.

Our label design will go on a 63mm tall frosted glass jar which is 62mm in diameter. The actual label dimensions should be, 170 mm (W) x 50 mm (H). The idea is so that it wraps around the whole jar with the design at one side (at the front) and the ingredients on another (at the back).

LABEL 1
Organic Polynesian Whipped Body Butter
Vanilla Bean
120ml

Made with Organic Shea and Cocoa Butters and exotic Monoi de Tahiti

Ingredients (INCI): Organic Raw Shea Butter (Butyrospermum Parkii), Organic Raw Cocoa Butter (Theobroma Cacao), Monoi de Tahiti (Coconut (Cocos nucifera) oil (and) Tiare (Gardenia tahitensis) flower), Organic Sweet Almond Oil (Prunus Amygdalus Dulcis), Organic Madagascan Vanilla Extract (Vanillin)

Handmade by Gently Velvety Ltd
14 Larkwell Lane, Bournemouth BH3 9QT, UK
Batch:

OPTIONAL WRITING (if it fits in):
100% Natural and Organic
Intensely Moisturising

LABEL 2
Mango Smoothie
120ml

Ingredients (INCI): Organic Raw Shea Butter (Butyrospermum Parkii), Organic Raw Cocoa Butter (Theobroma Cacao), Monoi de Tahiti (Coconut (Cocos nucifera) oil (and) Tiare (Gardenia tahitensis) flower), Organic Sweet Almond Oil (Prunus Amygdalus Dulcis), Organic Mango Flavour (Aroma)

Batch:

100% Natural and Organic
Intensely Moisturising

I have attached a picture of the jar we use and the lid we use for these products, as well as our logo. I've also attached a 'Handmade in Dorset' stamp which we'd like to go on there if possible, along with a shelf life symbol.

I am thinking the background colour of the labels will be either white or even brown paper colour. Perhaps it would be interesting to see it in both. UPDATE: We have decided on white background now, not brown.

The final design should denote handmade, organic, high quality, pure, yet quirky and original / unique. I am thinking perhaps a seemingly hand-drawn black leaf outline? Could fit the bill, but as I say, up to you. Something that says handmade yet professional.

I'd like to have the original Photoshop files from the winning designer so we can use them as a template for the rest of our horizontal labels.
Updates

Project Deadline Extended
Reason: Just need a few more days for designs we like to be worked on further, and to review new designs!

Target Market(s)

Everyone that appreciates a good quality skincare product focusing on natural & organic. Price is mid-range to high

Industry/Entity Type

It Company

Requirements
Must have
• Must make the product look high quality & organic yet quirky and accessible. Must have our logo and the shelf life symbol and the writing as above.
Nice to have
• Nice to have the 'handmade' stamp attached, but not absolutely necessary if it doesn't fit within your design.

```html
<!DOCTYPE html>
<html lang="en">
<head>
<meta charset="utf-8">
<title>Gently Velvety – Whipped Body Butter Labels</title>
<link href="https://fonts.googleapis.com/css2?family=Dosis:wght@400;500;600&family=Great+Vibes&display=swap" rel="stylesheet">
<style>
  :root {
    --backdrop: #e2e2e2;
    --label-white: #fbfcfb;
    --ink-grey: #858585;
    --ink-grey-dark: #767676;
    --script-brown: #3a1712;
    --vanilla-band: #ecb400;
    --mango-band: #e8312e;
    --vanilla-photo-a: #f7e34a;
    --vanilla-photo-b: #4a2e22;
    --mango-photo-a: #f2b233;
    --mango-photo-b: #d8443a;
  }
  * { margin: 0; padding: 0; box-sizing: border-box; }
  html, body {
    width: 1200px;
    height: 900px;
    overflow: hidden;
    background: var(--backdrop);
  }
  .canvas {
    position: relative;
    width: 1200px;
    height: 900px;
    display: flex;
    justify-content: center;
    align-items: center;
    gap: 40px;
  }
  .label-front {
    position: relative;
    width: 540px;
    height: 400px;
    background: var(--label-white);
    border-radius: 6px;
    box-shadow: 0 6px 18px rgba(0,0,0,0.08);
    font-family: "Dosis", sans-serif;
    color: var(--ink-grey);
  }
  .brand {
    position: absolute;
    left: 28px;
    top: 60px;
    display: flex;
    align-items: center;
    gap: 8px;
  }
  .brand-dot {
    width: 12px;
    height: 12px;
    border-radius: 50%;
    background: var(--ink-grey-dark);
  }
  .brand-name {
    font-family: "Dosis", sans-serif;
    font-weight: 600;
    font-size: 30px;
    line-height: 1;
    color: var(--ink-grey-dark);
    text-transform: uppercase;
    width: 130px;
  }
  .product-type {
    position: absolute;
    right: 30px;
    top: 70px;
    text-align: center;
    width: 300px;
  }
  .product-type .range {
    font-weight: 400;
    font-size: 22px;
    letter-spacing: 0.2px;
  }
  .product-type .kind {
    font-weight: 600;
    font-size: 34px;
    color: var(--ink-grey-dark);
    line-height: 1.1;
  }
  .flavour-band {
    position: absolute;
    right: 20px;
    top: 168px;
    width: 340px;
    height: 80px;
    border-radius: 4px 14px 6px 18px;
    display: flex;
    align-items: center;
    justify-content: flex-end;
    padding-right: 16px;
  }
  .flavour-band.vanilla { background: var(--vanilla-band); }
  .flavour-band.mango { background: var(--mango-band); }
  .flavour-name {
    font-family: "Great Vibes", cursive;
    font-size: 52px;
    color: var(--script-brown);
    white-space: nowrap;
  }
  .ingredient-photo {
    position: absolute;
    left: 30px;
    top: 160px;
    width: 190px;
    height: 150px;
    border-radius: 50%;
  }
  .ingredient-photo.vanilla {
    background: radial-gradient(circle at 55% 45%, var(--vanilla-photo-a) 0 38%, var(--vanilla-photo-b) 75%, transparent 76%);
  }
  .ingredient-photo.mango {
    background: radial-gradient(circle at 45% 45%, var(--mango-photo-b) 0 30%, var(--mango-photo-a) 55%, transparent 72%);
  }
  .claims {
    position: absolute;
    right: 40px;
    top: 272px;
    width: 300px;
    text-align: center;
    font-size: 24px;
    line-height: 1.3;
  }
  .claims .secondary {
    font-weight: 600;
    color: var(--ink-grey-dark);
  }
</style>
</head>
<body>
  <main class="canvas">
    <section class="label-front">
      <div class="brand">
        <span class="brand-dot"></span>
        <span class="brand-name">Gently Velvety</span>
      </div>
      <div class="product-type">
        <p class="range">ORGANIC POLYNESIAN WHIPPED</p>
        <p class="kind">BODY BUTTER</p>
      </div>
      <div class="flavour-band vanilla">
        <span class="flavour-name">Vanilla Bean</span>
      </div>
      <div class="ingredient-photo vanilla" role="img" aria-label="Photo of a yellow vanilla orchid flower with dark vanilla pods and leaves"></div>
      <div class="claims">
        <p>INTENSELY MOISTURISING</p>
        <p class="secondary">NATURAL &amp; ORGANIC</p>
      </div>
    </section>

    <section class="label-front">
      <div class="brand">
        <span class="brand-dot"></span>
        <span class="brand-name">Gently Velvety</span>
      </div>
      <div class="product-type">
        <p class="range">ORGANIC POLYNESIAN WHIPPED</p>
        <p class="kind">BODY BUTTER</p>
      </div>
      <div class="flavour-band mango">
        <span class="flavour-name">Mango Smoothie</span>
      </div>
      <div class="ingredient-photo mango" role="img" aria-label="Photo of a ripe red and yellow mango with a cubed mango half and a leaf"></div>
      <div class="claims">
        <p>INTENSELY MOISTURISING</p>
        <p class="secondary">NATURAL &amp; ORGANIC</p>
      </div>
    </section>
  </main>
</body>
</html>
```